Civora - a Political Plebescite app.

There is a current app in the App Store (worldwide) and Play Store (worldwide) called yourTally (with an owl logo). The UX needs to be redesigned to make it more visually pleasing.

The requirement is to build a UX that is suitable for both iOS and Android - i.e. consistent look for both platforms. The design is to span the variety of sizes available from smart devices - phones and tablets. The layout as it stands is portrait only, and a secondary design to encompass landscape is wanted.

You would need to download the app to get a feel for all the functionality - there are 3 visible forms (currently) and a hidden form, that will be used in the near future - this hidden form will look similar to the main (first) form.

To get full functionality you need to do the following:
Go to the Options page
Toggle the top slide
Click on UNREGISTERED
Select a state/territory

I know this is a bit non-intuitive - in the "real" product these steps are automated - but for this release the user gets to choose.

Once this is done - the other button(s) appear in the top left of the screen - and data is available to be displayed.

The current forms are included in this brief. The Options screen will ultimately not be showing all the current data, only the lower slider (or other indicator) and the associated version and copyright notices. The hidden screen is much like the main screen - showing the name of the bill and information pertaining to that bill - there needs to be a button (or action site) to toggle between the main and this hidden screen.

Target Market(s)

All eligable voters (currently in Australia)

Industry/Entity Type

Political

Requirements
Should not have
• Do not present to me my own/existing design with the only change being colours and label layout.

```html
<!DOCTYPE html>
<html lang="en">
<head>
<meta charset="utf-8">
<title>yourTally – Navigation Menu</title>
<link href="https://fonts.googleapis.com/css2?family=Open+Sans:wght@300;400;700&display=swap" rel="stylesheet">
<style>
  :root {
    --brand-blue: #3a9de0;
    --panel-dark: #333333;
    --row-dark: #393939;
    --header-white: #ffffff;
    --text-light: #e6e6e6;
    --nav-white: #ffffff;
  }
  * { box-sizing: border-box; margin: 0; padding: 0; }
  html, body { width: 750px; height: 1200px; overflow: hidden; }
  body {
    position: relative;
    background: var(--panel-dark);
    font-family: "Open Sans", Arial, sans-serif;
  }
  .side-strip {
    position: absolute; left: 638px; top: 0;
    width: 112px; height: 1200px;
    background: var(--brand-blue);
  }
  .menu-toggle {
    position: absolute; left: 663px; top: 28px;
    width: 64px; height: 64px;
  }
  .app-header {
    position: absolute; left: 0; top: 0;
    width: 638px; height: 116px;
    background: var(--header-white);
    display: flex; align-items: center;
    padding-left: 38px;
  }
  .brand-mark {
    width: 100px; height: 100px;
    border: 2px solid var(--brand-blue);
    border-radius: 50%;
    flex: none;
  }
  .brand-name {
    margin-left: 12px;
    color: var(--brand-blue);
    font-weight: 700;
    line-height: 1.15;
  }
  .brand-name .title { display: block; font-size: 36px; }
  .brand-name .sub { display: block; font-size: 25px; }
  .menu { position: absolute; left: 0; top: 0; width: 638px; }
  .menu-item {
    position: absolute; left: 0;
    width: 619px; height: 95px;
    background: var(--row-dark);
    display: flex; align-items: center;
    color: var(--text-light);
    font-size: 33px; font-weight: 300;
  }
  .menu-item.is-active { background: var(--brand-blue); color: #fff; }
  .menu-item .icon {
    width: 76px; height: 76px;
    margin-left: 20px; margin-right: 22px;
    flex: none;
  }
  .item-account { top: 182px; }
  .item-info { top: 301px; }
  .item-news { top: 422px; }
  .item-stats { top: 546px; }
  .item-settings { top: 661px; width: 612px; }
  .system-nav {
    position: absolute; left: 0; top: 1105px;
    width: 638px; height: 60px;
  }
</style>
</head>
<body>
  <div class="side-strip"></div>
  <svg class="menu-toggle" viewBox="0 0 64 64" aria-label="Menu">
    <circle cx="32" cy="32" r="29" fill="none" stroke="#fff" stroke-width="2"/>
    <g stroke="#fff" stroke-width="2">
      <line x1="18" y1="22" x2="46" y2="22"/>
      <line x1="18" y1="32" x2="46" y2="32"/>
      <line x1="18" y1="42" x2="46" y2="42"/>
    </g>
  </svg>

  <header class="app-header">
    <div class="brand-mark"></div>
    <div class="brand-name">
      <span class="title">yourTally</span>
      <span class="sub">Civora</span>
    </div>
  </header>

  <nav class="menu">
    <div class="menu-item item-account">
      <svg class="icon" viewBox="0 0 76 76" fill="none" stroke="#3a9de0" stroke-width="2">
        <circle cx="34" cy="36" r="30"/>
        <path d="M34 16c-8 0-12 6-12 13 0 6 3 11 8 13v5c-8 2-14 6-16 12"/>
        <path d="M34 16c8 0 12 6 12 13 0 4-1 7-3 9"/>
        <circle cx="54" cy="56" r="6"/>
        <circle cx="54" cy="56" r="11" stroke-dasharray="4 3"/>
      </svg>
      <span>Unregistered</span>
    </div>
    <div class="menu-item item-info is-active">
      <svg class="icon" viewBox="0 0 76 76">
        <circle cx="38" cy="38" r="30" fill="#fff"/>
        <circle cx="40" cy="24" r="4" fill="#3a9de0"/>
        <path d="M32 33h10l-5 18c-1 3 1 3 5 1l-1 3c-6 3-12 3-11-2l4-16h-3z" fill="#3a9de0"/>
      </svg>
      <span>Info</span>
    </div>
    <div class="menu-item item-news">
      <svg class="icon" viewBox="0 0 76 76" fill="none" stroke="#3a9de0" stroke-width="2.5">
        <path d="M14 12h44v52H18a4 4 0 0 1-4-4z"/>
        <path d="M58 24h4v38a2 2 0 0 1-4 2"/>
        <rect x="20" y="24" width="16" height="14"/>
        <line x1="20" y1="18" x2="52" y2="18"/>
        <line x1="40" y1="26" x2="52" y2="26"/>
        <line x1="40" y1="32" x2="52" y2="32"/>
        <line x1="40" y1="38" x2="52" y2="38"/>
        <line x1="20" y1="46" x2="52" y2="46"/>
        <line x1="20" y1="52" x2="52" y2="52"/>
      </svg>
      <span>News</span>
    </div>
    <div class="menu-item item-stats">
      <svg class="icon" viewBox="0 0 76 76" fill="#3a9de0">
        <rect x="10" y="48" width="10" height="20" rx="2"/>
        <rect x="24" y="38" width="10" height="30" rx="2"/>
        <rect x="38" y="26" width="10" height="42" rx="2"/>
        <rect x="52" y="14" width="10" height="54" rx="2"/>
      </svg>
      <span>Stats</span>
    </div>
    <div class="menu-item item-settings">
      <svg class="icon" viewBox="0 0 76 76" fill="none" stroke="#3a9de0" stroke-width="2.5">
        <path d="M34 8h8l2 8 6 3 7-4 6 6-4 7 3 6 8 2v8l-8 2-3 6 4 7-6 6-7-4-6 3-2 8h-8l-2-8-6-3-7 4-6-6 4-7-3-6-8-2v-8l8-2 3-6-4-7 6-6 7 4 6-3z"/>
        <circle cx="38" cy="38" r="10"/>
      </svg>
      <span>Settings</span>
    </div>
  </nav>

  <svg class="system-nav" viewBox="0 0 638 60" fill="none" stroke="#fff" stroke-width="2.5" aria-label="System navigation">
    <path d="M157 18v24l-20-12z"/>
    <circle cx="377" cy="30" r="12"/>
    <rect x="595" y="19" width="22" height="22"/>
  </svg>
</body>
</html>
```